Business Card Design

I am starting my therapy private practice. I will be an in home therapist, so I go into family's homes instead of using an office to do family/marriage therapy. Therefore, I do not have an office address. I am looking for something in the black, red, gray, and blue color scheme that appeals to both families, couples and teenagers.

Industry/Entity Type

Business

Contact Information for Business Card

Lena Brightwell, MS, MFT Intern
Marriage and Family Therapy
In Home Therapist
617-482-5190
Lena@LenaBrightwell-example.com

```html
<!DOCTYPE html>
<html lang="en">
<head>
<meta charset="utf-8">
<title>Lena Brightwell – Business Card</title>
<link rel="stylesheet" href="https://fonts.googleapis.com/css2?family=Marcellus&family=Tenor+Sans&display=swap">
<style>
  :root {
    --page: #ffffff;
    --navy: #062b68;
    --rose: #e8567a;
    --white: #ffffff;
    --sky: #8fc6ea;
    --rule: #c9d3e6;
  }
  html, body {
    margin: 0;
    padding: 0;
    width: 1200px;
    height: 695px;
    overflow: hidden;
    background: var(--page);
  }
  .card {
    position: absolute;
    left: 178px;
    top: 100px;
    width: 854px;
    height: 495px;
    background: var(--navy);
    color: var(--white);
    font-family: "Tenor Sans", sans-serif;
  }
  .brand-mark {
    position: absolute;
    left: 183px;
    top: 187px;
    width: 58px;
    height: 58px;
    border: 5px solid var(--rose);
    box-sizing: border-box;
  }
  .brand-name {
    position: absolute;
    left: 0;
    width: 424px;
    top: 280px;
    text-align: center;
    font-family: "Marcellus", serif;
    font-variant: small-caps;
    font-size: 40px;
    letter-spacing: 0.5px;
    line-height: 1;
    white-space: nowrap;
  }
  .role-ribbon {
    position: absolute;
    left: 402px;
    top: 140px;
    width: 411px;
    height: 46px;
  }
  .role-ribbon span {
    position: absolute;
    inset: 0;
    display: flex;
    align-items: center;
    justify-content: center;
    font-size: 22px;
    letter-spacing: 1px;
    color: var(--white);
  }
  .credentials {
    position: absolute;
    left: 406px;
    top: 204px;
    width: 400px;
    margin: 0;
    font-size: 23px;
    line-height: 29px;
  }
  .rule {
    position: absolute;
    left: 402px;
    width: 405px;
    border-top: 1.5px dashed var(--rule);
  }
  .contact {
    position: absolute;
    left: 414px;
    display: flex;
    align-items: center;
    gap: 14px;
    font-size: 23px;
    white-space: nowrap;
  }
  .contact svg {
    width: 22px;
    height: 22px;
    flex: none;
  }
</style>
</head>
<body>
  <main class="card">
    <div class="brand-mark" aria-hidden="true"></div>
    <div class="brand-name">Lena Brightwell</div>

    <div class="role-ribbon">
      <svg width="411" height="46" viewBox="0 0 411 46" aria-hidden="true">
        <polygon points="0,0 411,0 389,23 411,46 0,46 22,23" fill="var(--rose)"/>
      </svg>
      <span>♥&nbsp; IN HOME THERAPIST &nbsp;♥</span>
    </div>

    <p class="credentials">MS, MFT Intern Marriage and Family Therapy</p>

    <div class="rule" style="top:279px"></div>

    <div class="contact" style="top:291px">
      <svg viewBox="0 0 24 24" aria-hidden="true">
        <circle cx="12" cy="12" r="10.5" fill="none" stroke="var(--sky)" stroke-width="1.6"/>
        <path d="M8.3 6.6l1.8-.4 1.2 2.7-1.2 1c.6 1.4 1.6 2.4 3 3l1-1.2 2.7 1.2-.4 1.8c-.2.6-.8 1-1.5.9-3.8-.5-6.8-3.5-7.3-7.3-.1-.7.3-1.3.7-1.7z" fill="none" stroke="var(--sky)" stroke-width="1.4" stroke-linejoin="round"/>
      </svg>
      <span>617-482-5190</span>
    </div>

    <div class="rule" style="top:334px"></div>

    <div class="contact" style="top:348px">
      <svg viewBox="0 0 24 24" aria-hidden="true">
        <path d="M3 10l9-6 9 6v10H3z" fill="none" stroke="var(--sky)" stroke-width="1.6" stroke-linejoin="round"/>
        <path d="M3 10l9 6 9-6M3 20l7-5.5M21 20l-7-5.5" fill="none" stroke="var(--sky)" stroke-width="1.4" stroke-linejoin="round"/>
      </svg>
      <span>Lena@LenaBrightwell-example.com</span>
    </div>
  </main>
</body>
</html>
```